Print & digital package needed for technology firm

We need a package of coordinating marketing materials for our technology business. We offer technology solutions to midsized organizations, including data center, outsourced IT, and technology consulting. Find more information on our website, www.pexlora.com. Design is the main concern, we can modify the text ongoing to best reflect our company’s offerings. The design should communicate technology expertise and strategic thinking. Our website is currently being updated with a “flat design” theme and we’d like design of these items to be flat, fresh, modern, and professional, without being boring.
Please use attached logo - can send in .ai/.eps/.psd/etc. Fonts in logo are Futura, Futura Book, and Lato. Please use pexLORA blue, #0372bb.
Please find attached one of our product flyers for one of the computers we lease. Fonts used are Roboto Slab (partial to this font) & Lato. Also attached copy of our business card design.
Taglines we have used include “Does IT hear what troubles you?” and “IT made simple” although we are open to new ideas.
Would like final products to be available in editable files - .psd/.tif/.ai/etc.

- 1 PowerPoint template
- 1 leaderboard ad (digital, 72dpi)
- 1 medium rectangle ad 300x250 (digital, 72dpi)
- 1 full page ad 8x11 (print, 300dpi)
- 1 half-page ad horizontal (print, 300dpi)
- 1 letterhead template
- 1 proposal front-page

There is potential for further graphic/print design opportunities for our business as well.

All, thank you for your assistance in understanding the budget process with this type of design contest - we have updated the project's budget to reflect the items we are requesting.

Please email mvarga at pexlora.com with inquiries or comments. Thank you.

Designers,

Due to an oversight, our project was listed as "refundable" - this has been corrected and changed to committed payment.
To enter into this contest, please pick 2-3 items from the list of desired materials (ads, powerpoint, letterhead, etc.) It is not necessary to submit all items which will be part of the final package to be considered for the contest.

Thank you. Please contact mvarga@pexlora.com for questions.
Best,
Mimi

CEOs, CFOs, CIOs, COOs - college+ educated, 30-60, professional.

```html
<!DOCTYPE html>
<html lang="en">
<head>
<meta charset="utf-8">
<title>About Company – pexLORA</title>
<link rel="stylesheet" href="https://fonts.googleapis.com/css2?family=Lato:wght@300;400;700&family=Roboto+Slab:wght@300;400&display=block">
<style>
  :root {
    --brand-blue: #0372bb;
    --brand-blue-dark: #035d9a;
    --slate: #58585a;
    --slate-dark: #4a4a4c;
    --ink: #2a2a2a;
    --paper: #ffffff;
  }
  * { box-sizing: border-box; margin: 0; padding: 0; }
  html, body {
    width: 1200px;
    height: 709px;
    overflow: hidden;
    background: var(--paper);
  }
  .page {
    position: relative;
    width: 1200px;
    height: 709px;
  }
  .title-band {
    position: absolute;
    left: 55px;
    top: 40px;
    width: 1100px;
    height: 68px;
  }
  .title-band svg {
    position: absolute;
    inset: 0;
  }
  .section-title {
    position: absolute;
    left: 87px;
    top: 14px;
    font-family: "Roboto Slab", "Rockwell", "Roboto", sans-serif;
    font-weight: 400;
    font-size: 34px;
    letter-spacing: 2.6px;
    line-height: 40px;
    color: var(--paper);
    white-space: nowrap;
  }
  .wordmark {
    position: absolute;
    right: 78px;
    top: 17px;
    font-family: "Lato", Arial, sans-serif;
    font-weight: 700;
    font-size: 31px;
    letter-spacing: -0.5px;
    line-height: 36px;
    color: var(--paper);
  }
  .body-copy {
    position: absolute;
    top: 145px;
    font-family: "Lato", Arial, sans-serif;
    font-weight: 300;
    font-size: 18px;
    line-height: 31.8px;
    color: var(--ink);
    white-space: nowrap;
  }
  .body-copy p + p { margin-top: 31.8px; }
  .column-left { left: 74px; }
  .column-right { left: 600px; }
</style>
</head>
<body>
<main class="page">
  <header class="title-band">
    <svg width="1100" height="68" viewBox="0 0 1100 68" aria-hidden="true">
      <polygon points="0,0 920,0 852,68 0,68" fill="var(--brand-blue)"/>
      <polygon points="0,0 135,0 67,68 0,68" fill="var(--brand-blue-dark)"/>
      <polygon points="0,0 68,0 0,68" fill="var(--slate)"/>
      <polygon points="68,0 135,0 67,68 0,68" fill="var(--slate)" opacity="0.45"/>
      <polygon points="850,0 920,0 852,68 782,68" fill="var(--brand-blue-dark)"/>
      <polygon points="920,0 1100,0 1032,68 852,68" fill="var(--slate)"/>
      <polygon points="850,0 920,0 852,68" fill="var(--slate-dark)" opacity="0.5"/>
    </svg>
    <h1 class="section-title">About Company</h1>
    <div class="wordmark">pexLORA</div>
  </header>

  <section class="body-copy column-left">
    <p>Lorem ipsum dolor sit amet, consectetur adipiscing elit.<br>
    Aenean dignissim arcu non luctus luctus. Etiam dolor<br>
    tellus, eleifend at mauris nec, tempus tincidunt nibh. Etiam<br>
    a velit eu mi porta suscipit. Ut vitae mollis velit. Nulla vitae<br>
    nibh sed tellus venenatis aliquam quis quis dui. Sed sed ul-<br>
    trices nibh. Quisque accumsan elementum sapien, non<br>
    dignissim quam ultrices ac. In sit amet tortor vel metus in-<br>
    terdum semper in vitae velit. Donec tellus justo, rhoncus ut<br>
    pulvinar et, egestas sed odio. Proin lorem justo, viverra ac-<br>
    cumsan sem eu, dictum dapibus nisi. Nam orci velit, biben-<br>
    dum vel ultrices sit amet, aliquet nec orci. Vivamus eget<br>
    neque vel mi suscipit consequat. Maecenas non libero<br>
    tempus nisl iaculis rutrum in vitae metus. Sed eu tempor<br>
    felis, nec lacinia est. Etiam purus nisi, molestie a risus vel,<br>
    sagittis hendrerit ante. Aenean eu mattis ipsum.</p>
    <p>Sed interdum vestibulum neque, ultricies posuere est lob-</p>
  </section>

  <section class="body-copy column-right">
    <p>a. Fusce interdum ipsum vel eleifend rhoncus. Suspendisse po-<br>
    tenti. Vestibulum hendrerit eros massa, non posuere velit sollici-<br>
    tudin ut. Proin sed mattis ligula, id mattis risus. Pellentesque ha-<br>
    bitant morbi tristique senectus et netus et malesuada fames ac<br>
    turpis egestas. Cras sem diam, bibendum ac rhoncus ac, egestas<br>
    ac metus. Curabitur imperdiet mi odio, eget consequat sapien<br>
    tempor id. Nunc pellentesque urna et lacus ultricies dictum.</p>
  </section>
</main>
</body>
</html>
```